Retirement Plan Advisor Bio

See the attached document and photo for content. I would like someone to design this one page flyer using my logo. This logo was designed by a designer with craft nest. I am looking for a professional looking document. I want to he color scheme to be primarily white and gold.

Target Market(s)

Employers who offer a retirement plan

Requirements
Should not have
• The designs that I have received look more like resumes. I am interested in advertising my Retirement plan services. If anyone can change their submissions and change it to an ad for retirement plan services instead of a Bio or resume, I would prefer that.

```html
<!DOCTYPE html>
<html lang="en">
<head>
<meta charset="utf-8">
<title>Retirement Plan Advisor Flyer</title>
<link rel="stylesheet" href="https://fonts.googleapis.com/css2?family=Oswald:wght@600&family=Roboto:wght@400;500&family=Roboto+Condensed:wght@500;700&display=swap">
<style>
  :root {
    --gold: #b8915a;
    --gold-light: #d2ad72;
    --gold-dark: #8d6a36;
    --ink: #1e1e1e;
    --text: #2e2e2e;
    --paper: #ffffff;
    --mist: #efefef;
    --stage: #2a2a2a;
  }
  * { margin: 0; padding: 0; box-sizing: border-box; }
  html, body { width: 1200px; height: 546px; overflow: hidden; }
  body { background: var(--stage); font-family: "Roboto", Arial, sans-serif; color: var(--text); }

  .flyer {
    position: absolute; left: 398px; top: 13px;
    width: 404px; height: 520px;
    background: var(--paper); overflow: hidden;
  }
  .flyer-shapes { position: absolute; inset: 0; }

  .brand {
    position: absolute; left: 20px; top: 32px;
    display: flex; align-items: center; gap: 7px;
  }
  .brand-square { width: 16px; height: 16px; background: var(--gold); }
  .brand-name { font-family: "Roboto", Arial, sans-serif; font-weight: 500; font-size: 15px; color: var(--gold-dark); letter-spacing: 0.2px; }

  .advisor { position: absolute; left: 19px; top: 98px; color: var(--paper); }
  .advisor-name { font-family: "Oswald", "Roboto Condensed", sans-serif; font-weight: 600; font-size: 36px; line-height: 1; letter-spacing: 0.2px; }
  .advisor-title { margin-top: 7px; font-size: 11px; line-height: 1.3; }

  .mission {
    position: absolute; left: 19px; top: 190px; width: 212px;
    color: var(--paper); font-size: 9px; line-height: 12.6px;
  }

  .section-heading {
    display: flex; align-items: center; gap: 5px;
    font-family: "Roboto Condensed", Arial, sans-serif; font-weight: 700; font-size: 13px;
    color: var(--gold); margin-bottom: 9px;
  }
  .section-heading .mark { width: 8px; height: 8px; background: var(--gold); margin-right: 2px; }
  .section-heading .strong { color: var(--ink); }

  .specialties { position: absolute; left: 18px; top: 284px; width: 178px; }
  .qualifications { position: absolute; left: 210px; top: 284px; width: 180px; }

  .checklist { list-style: none; position: relative; }
  .checklist::before {
    content: ""; position: absolute; left: 4.5px; top: 6px; bottom: 12px; width: 1px; background: var(--gold);
  }
  .checklist li {
    position: relative; padding-left: 18px; margin-bottom: 5px;
    font-size: 7.2px; line-height: 8.8px; color: var(--text);
  }
  .checklist li::before {
    content: ""; position: absolute; left: 0; top: 0;
    width: 10px; height: 10px; border-radius: 50%; background: var(--gold);
  }
  .checklist li::after {
    content: ""; position: absolute; left: 3px; top: 2.5px;
    width: 4px; height: 2.5px; border-left: 1.3px solid #fff; border-bottom: 1.3px solid #fff;
    transform: rotate(-45deg);
  }

  .education { position: absolute; left: 0; top: 410px; width: 404px; height: 62px; background: var(--mist); }
  .education-icon {
    position: absolute; left: 13px; top: 13px; width: 34px; height: 34px; border-radius: 50%;
    border: 1.5px solid #9a9a9a; background: #f7f7f7;
  }
  .education-body { position: absolute; left: 58px; top: 7px; width: 340px; }
  .education-heading { font-family: "Roboto Condensed", Arial, sans-serif; font-weight: 700; font-size: 13px; color: var(--gold); }
  .education-degree { font-size: 7.8px; color: var(--gold); margin-top: 3px; font-weight: 500; }
  .disclosure { font-size: 6.7px; line-height: 8.4px; color: var(--text); margin-top: 3px; }

  .footer { position: absolute; left: 0; top: 472px; width: 404px; height: 48px; background: var(--ink); }
  .footer-cta {
    position: absolute; left: 0; top: 0; width: 74px; height: 48px;
    padding: 10px 0 0 9px;
    background: linear-gradient(90deg, var(--gold-dark), var(--gold-light));
    clip-path: polygon(0 0, 60px 0, 74px 48px, 0 48px);
    font-family: "Roboto Condensed", Arial, sans-serif; font-weight: 700; font-size: 8.6px; line-height: 9.4px; color: var(--ink);
  }
  .footer-phone {
    position: absolute; left: 80px; top: 8px; display: flex; align-items: center; gap: 5px;
    font-family: "Roboto Condensed", Arial, sans-serif; font-weight: 700; font-size: 25px; color: var(--paper);
  }
  .footer-divider { position: absolute; left: 262px; top: 10px; width: 1px; height: 28px; background: #555; }
  .footer-contacts { position: absolute; left: 269px; top: 9px; list-style: none; }
  .footer-contacts li { display: flex; align-items: center; gap: 5px; font-size: 7px; line-height: 10px; color: var(--paper); }
  .footer-contacts .dot { width: 6px; height: 6px; border-radius: 50%; background: var(--gold); }
</style>
</head>
<body>
<main class="flyer">
  <svg class="flyer-shapes" width="404" height="520" viewBox="0 0 404 520">
    <defs>
      <linearGradient id="goldBand" x1="0" y1="0" x2="1" y2="0">
        <stop offset="0" stop-color="#8d6a36"/>
        <stop offset="0.55" stop-color="#b8915a"/>
        <stop offset="1" stop-color="#d2ad72"/>
      </linearGradient>
      <linearGradient id="goldStripe" x1="0" y1="0" x2="1" y2="1">
        <stop offset="0" stop-color="#d2ad72"/>
        <stop offset="1" stop-color="#8d6a36"/>
      </linearGradient>
      <linearGradient id="darkBand" x1="0" y1="0" x2="1" y2="0">
        <stop offset="0" stop-color="#2c2c2c"/>
        <stop offset="1" stop-color="#141414"/>
      </linearGradient>
      <linearGradient id="portraitTone" x1="0" y1="0" x2="0.4" y2="1">
        <stop offset="0" stop-color="#e6dcc4"/>
        <stop offset="0.45" stop-color="#d6bf93"/>
        <stop offset="0.75" stop-color="#4a4440"/>
        <stop offset="1" stop-color="#1c1c1c"/>
      </linearGradient>
    </defs>
    <rect x="0" y="88" width="404" height="90" fill="url(#goldBand)"/>
    <rect x="0" y="178" width="404" height="91" fill="url(#darkBand)"/>
    <polygon points="275,0 404,0 404,210 350,269 235,269 252,88" fill="url(#portraitTone)" role="img" aria-label="Portrait photo of the advisor in a dark blazer"/>
    <polygon points="236,0 275,0 252,88 200,88" fill="url(#goldStripe)"/>
    <polygon points="404,222 404,330 350,269" fill="url(#goldStripe)"/>
    <polygon points="404,210 404,222 350,269 344,269" fill="#ffffff"/>
    <line x1="201" y1="286" x2="201" y2="402" stroke="#e2e2e2" stroke-width="1"/>
  </svg>

  <div class="brand">
    <span class="brand-square"></span>
    <span class="brand-name">Verra Financial, LLC</span>
  </div>

  <header class="advisor">
    <h1 class="advisor-name">HELEN R VOSS</h1>
    <p class="advisor-title">RPC · IFS<br>Northgate Financial Advisor</p>
  </header>

  <p class="mission">I strive to improve retirement outcomes for my plan sponsor clients and their employees through careful retirement plan design assistance, strategic and targeted communication and education, as well as continual monitoring of results.</p>

  <section class="specialties">
    <h2 class="section-heading"><span class="mark"></span>Professional<span class="strong">Specialties</span></h2>
    <ul class="checklist">
      <li>Over 18 years of experience in the retirement plan industry</li>
      <li>Focused on helping plan sponsors reduce administrative burdens and fiduciary risk</li>
      <li>Dedicated to helping employees work toward a positive retirement outcome through careful analysis of their savings rate, investment strategy and overall financial wellness</li>
    </ul>
  </section>

  <section class="qualifications">
    <h2 class="section-heading"><span class="mark"></span>Qualifications</h2>
    <ul class="checklist">
      <li>Retirement Planning Counselor</li>
      <li>Institutional Fiduciary Specialist</li>
      <li>Investment Advisor Representative</li>
      <li>Series 7, 63, and 65 Securities licenses with Northgate Financial</li>
      <li>Holds Life and Health Insurance licenses from Illinois</li>
    </ul>
  </section>

  <section class="education">
    <div class="education-icon" role="img" aria-label="Education icon"></div>
    <div class="education-body">
      <h2 class="education-heading">Education</h2>
      <p class="education-degree">BS Halford University, 1987</p>
      <p class="disclosure">*Securities and Investment Advisory Services offered through Northgate Financial Holdings, Inc, a Registered Broker/Dealer and Investment Advisor, member of industry regulatory bodies</p>
    </div>
  </section>

  <footer class="footer">
    <p class="footer-cta">For More<br>Information<br>Contact :</p>
    <div class="footer-phone">
      <svg width="16" height="20" viewBox="0 0 16 20" aria-hidden="true">
        <rect x="3" y="1" width="10" height="18" rx="2" fill="none" stroke="#b8915a" stroke-width="2"/>
        <line x1="6" y1="16" x2="10" y2="16" stroke="#b8915a" stroke-width="1.5"/>
      </svg>
      <span>(555) 204.7180</span>
    </div>
    <span class="footer-divider"></span>
    <ul class="footer-contacts">
      <li><span class="dot"></span>240 Maple Ridge Rd. Fairview, IL 60999</li>
      <li><span class="dot"></span>helen.voss@northgate.com</li>
      <li><span class="dot"></span>www.helenvoss.com</li>
    </ul>
  </footer>
</main>
</body>
</html>
```